New webpage design for development bureau

We are a development bureau in Denmark, and need a design for our webpage. We are called Harbor Development (Part of Harbor Fjeld Skolium Group), and are going to aim for multiple markets: Web, Apps, Desktop applications, ect.

We already have a logo, see the uploaded file. We do not have any special demands, other than in have to be simple. A portfolio view should also be available, for future customers.

```html
<!DOCTYPE html>
<html lang="en">
<head>
<meta charset="utf-8">
<title>Harbor Development</title>
<link href="https://fonts.googleapis.com/css2?family=Oswald:wght@500;600;700&family=Nunito+Sans:wght@300;400;600&family=Dancing+Script:wght@700&display=swap" rel="stylesheet">
<style>
:root{
  --blue:#0b85cf;
  --sky:#5cc2f2;
  --orange:#f55f0a;
  --ink:#1e1e1e;
  --grey:#7a7a7a;
  --footer:#222;
  --footer-text:#9a9a9a;
  --tw:#55c6f4;
  --fb:#3d7dd6;
  --gp:#ea5c5c;
  --rss:#f8b42c;
}
*{box-sizing:border-box;margin:0;padding:0}
html,body{width:1134px;height:1200px;overflow:hidden;background:#fff}
body{position:relative;font-family:"Nunito Sans",Arial,sans-serif;color:var(--ink)}
.abs{position:absolute}
.head-font{font-family:"Oswald",Arial,sans-serif}

/* header */
.brand{left:189px;top:18px;font-family:"Oswald",Arial,sans-serif;font-weight:700;font-size:27px;letter-spacing:0.5px;color:var(--ink)}
.join{left:746px;top:10px;font-family:"Dancing Script",cursive;font-size:16px;color:#666}
.social-top{left:833px;top:10px;display:flex;gap:5px}
.social-top span{width:24px;height:24px;display:block}
.utility{left:712px;top:44px;display:flex;font-size:10.5px;color:#666;background:#f6f6f6;height:20px;align-items:center}
.utility span{padding:0 10px;border-right:1px solid #e2e2e2;display:flex;align-items:center;gap:4px}
.utility span:last-child{border-right:0}

/* nav */
.nav{left:0;top:73px;width:1134px;height:29px;background:var(--blue)}
.nav ul{list-style:none;display:flex;position:absolute;left:190px;top:7px;color:#fff;font-size:12px;font-weight:600}
.nav li{margin-right:17px}
.nav li.sep{font-weight:400}

/* hero */
.hero{left:0;top:102px;width:1134px;height:278px;background:linear-gradient(180deg,#f4f4f4,#ebebeb)}
.hero-rule{left:0;top:380px;width:1134px;height:3px;background:var(--blue)}
.hero-title{left:215px;top:140px;font-family:"Oswald",Arial,sans-serif;font-weight:600;font-size:38px;line-height:46px;color:var(--orange);font-variant:small-caps;letter-spacing:0.5px}
.btn-view{left:215px;top:306px;width:115px;height:32px;background:var(--blue);color:#fff;font-size:13px;font-weight:600;display:flex;align-items:center;justify-content:center;gap:8px}
.portrait{left:632px;top:76px;width:262px;height:304px;background:radial-gradient(ellipse at 50% 35%,#d9b7a2 0,#bcd8ee 40%,#8fbfe3 70%,rgba(235,235,235,0) 100%)}
.dots{left:548px;top:358px;display:flex;gap:5px}
.dots i{width:10px;height:10px;border-radius:50%;background:#222;display:block}
.dots i.on{background:#fff;border:3px solid #222}

/* sections */
.section-title{left:0;width:1134px;text-align:center;font-family:"Oswald",Arial,sans-serif;font-weight:600;font-size:28px;letter-spacing:0.3px}
.section-title em{font-style:normal;color:var(--sky)}
.about-text{left:189px;top:457px;width:756px;text-align:center;font-size:13.5px;line-height:19px;color:var(--grey);font-weight:300}
.btn-orange{background:var(--orange);color:#fff;font-size:12.5px;display:flex;align-items:center;justify-content:center;outline:1px dotted rgba(255,255,255,.6);outline-offset:-3px}
.btn-dark{background:#222;color:#fff;font-size:11.5px;display:flex;align-items:center;justify-content:center;outline:1px dotted rgba(255,255,255,.5);outline-offset:-3px}

.card{top:674px;width:241px;height:132px;background:radial-gradient(ellipse at 50% 45%,#fff 30%,#e6f2fb 100%);box-shadow:0 6px 6px -4px rgba(0,0,0,.12)}
.card.active{background:var(--orange)}
.card h3{position:absolute;left:0;bottom:27px;width:100%;text-align:center;font-family:"Oswald",Arial,sans-serif;font-weight:600;font-size:14px;letter-spacing:0.3px}
.card.active h3{color:#fff}
.card svg{position:absolute;left:50%;top:24px;transform:translateX(-50%)}
.card-text{top:823px;width:241px;font-size:10.8px;line-height:15px;color:var(--grey)}

/* footer */
.footer{left:0;top:973px;width:1134px;height:227px;background:var(--footer)}
.foot-h{font-family:"Oswald",Arial,sans-serif;font-weight:600;font-size:14px;color:#fff;top:994px}
.sitemap{left:189px;top:1022px;list-style:none;font-size:10.5px;line-height:21px;color:var(--footer-text)}
.sitemap li:first-child{color:#fff}
.share{left:383px;top:1018px;list-style:none;font-size:10.5px;color:var(--footer-text)}
.share li{display:flex;align-items:center;gap:8px;height:24px}
.share li:first-child{color:#fff}
.share span{width:21px;height:21px;display:block}
.map{left:583px;top:1018px;width:192px;height:97px;background:linear-gradient(135deg,#eceae4,#dcdad3)}
.address{left:790px;top:1017px;color:#fff;font-size:11.5px;font-weight:600;line-height:18px}
.contact{left:790px;top:1072px;color:var(--footer-text);font-size:9.5px;line-height:15px}
.copyright{left:458px;top:1150px;width:219px;height:26px;border:1px solid #3a3a3a;border-radius:13px;background:#1c1c1c;color:#777;font-size:10px;display:flex;align-items:center;justify-content:center}
</style>
</head>
<body>

<header>
  <div class="abs brand">HARBOR</div>
  <div class="abs join">Join us now!</div>
  <div class="abs social-top" aria-label="Social links">
    <span style="background:var(--tw)"></span>
    <span style="background:var(--fb)"></span>
    <span style="background:var(--gp)"></span>
    <span style="background:var(--rss)"></span>
  </div>
  <div class="abs utility">
    <span><svg width="9" height="9" viewBox="0 0 10 10"><circle cx="5" cy="3" r="2.4" fill="#666"/><path d="M0.5 10 Q5 4 9.5 10Z" fill="#666"/></svg>Client Portal</span>
    <span><svg width="9" height="9" viewBox="0 0 10 10"><path d="M0 0H10V7H4L1 10V7H0Z" fill="#666"/></svg>Chat</span>
    <span><svg width="6" height="9" viewBox="0 0 6 10"><rect x="0.5" y="0.5" width="5" height="9" rx="1" fill="none" stroke="#666"/></svg>+45 3312 4870</span>
  </div>
</header>

<nav class="abs nav">
  <ul>
    <li>Home</li><li class="sep">–</li>
    <li>About</li><li class="sep">–</li>
    <li>Servies</li><li class="sep">–</li>
    <li>Portfolio</li><li class="sep">–</li>
    <li>Contact Us</li>
  </ul>
</nav>

<section>
  <div class="abs hero"></div>
  <div class="abs portrait" role="img" aria-label="Photo of a smiling young developer in a light blue shirt and tie, arms crossed"></div>
  <h1 class="abs hero-title">Welcome to IT<br>Harbor Development<br>Company</h1>
  <div class="abs btn-view">View More
    <svg width="14" height="14" viewBox="0 0 14 14"><circle cx="7" cy="7" r="7" fill="#fff"/><path d="M5.5 3.8 8.7 7 5.5 10.2" stroke="var(--blue)" stroke-width="2" fill="none"/></svg>
  </div>
  <div class="abs dots"><i></i><i class="on"></i><i></i></div>
  <div class="abs hero-rule"></div>
</section>

<section>
  <h2 class="abs section-title" style="top:410px"><em>ABOUT US</em> HARBOR</h2>
  <p class="abs about-text">Lorem Ipsum is simply dummy text of the printing and typesetting industry. Lorem Ipsum has been the industry's standard dummy text ever since the 1500s, when an unknown printer took a galley of type and scrambled it to make a type specimen book. It has survived not only five centuries, but also the leap into electronic typesetting</p>
  <div class="abs btn-orange" style="left:506px;top:528px;width:122px;height:32px">READ MORE</div>
</section>

<section>
  <h2 class="abs section-title" style="top:612px"><em>OUR</em> SERVICES</h2>

  <div class="abs card" style="left:189px">
    <svg width="62" height="54" viewBox="0 0 62 54"><rect x="2" y="2" width="58" height="40" fill="none" stroke="var(--ink)" stroke-width="3"/><rect x="24" y="44" width="14" height="4" fill="var(--ink)"/><rect x="16" y="48" width="30" height="3" fill="var(--ink)"/><text x="31" y="30" text-anchor="middle" font-family="Nunito Sans, sans-serif" font-size="18" fill="var(--ink)">&lt;/&gt;</text></svg>
    <h3>WEB</h3>
  </div>
  <div class="abs card active" style="left:447px">
    <svg width="76" height="56" viewBox="0 0 76 56"><circle cx="24" cy="28" r="17" fill="none" stroke="#fff" stroke-width="8" stroke-dasharray="7 4"/><circle cx="24" cy="28" r="7" fill="#fff"/><path d="M34 46 L66 10 L72 16 L40 52 L31 55Z" fill="#fff"/></svg>
    <h3>APPS</h3>
  </div>
  <div class="abs card" style="left:704px">
    <h3>DESKTOP APPLICATIONS</h3>
  </div>

  <p class="abs card-text" style="left:189px">There are many variations of passages of Lorem Ipsum available, but the majority have suffered alteration in some form, by injected humour, or randomised words which don't look even slightly believable.</p>
  <p class="abs card-text" style="left:446px">There are many variations of passages of Lorem Ipsum available, but the majority have suffered alteration in some form, by injected humour, or randomised words which don't look even slightly believable.</p>
  <p class="abs card-text" style="left:704px">There are many variations of passages of Lorem Ipsum available, but the majority have suffered alteration in some form, by injected humour, or randomised words which don't look even slightly believable.</p>

  <div class="abs btn-dark" style="left:189px;top:916px;width:93px;height:27px">READ MORE</div>
  <div class="abs btn-orange" style="left:446px;top:916px;width:93px;height:27px;font-size:11.5px">READ MORE</div>
  <div class="abs btn-dark" style="left:704px;top:916px;width:93px;height:27px">READ MORE</div>
</section>

<footer>
  <div class="abs footer"></div>
  <h4 class="abs foot-h" style="left:190px">SITEMAP</h4>
  <ul class="abs sitemap">
    <li>Home</li><li>About Us</li><li>Services</li><li>Portfolio</li><li>Contact Us</li>
  </ul>
  <h4 class="abs foot-h" style="left:383px">SHARE US ON</h4>
  <ul class="abs share">
    <li><span style="background:var(--fb)"></span>Friendnet</li>
    <li><span style="background:var(--tw)"></span>Chirper</li>
    <li><span style="background:var(--gp)"></span>Circles +</li>
    <li><span style="background:var(--rss)"></span>Rss</li>
  </ul>
  <h4 class="abs foot-h" style="left:582px">CONTACT US</h4>
  <div class="abs map" role="img" aria-label="Street map showing the office location"></div>
  <div class="abs address">Unit 2 Kajvej 14<br>8000 Aarhus C</div>
  <div class="abs contact">Phone : +45 3312 4870<br>Mobile : +45 3312 4871<br>Email : hello@harbordev.dk</div>
  <div class="abs copyright">© 2014 Harbor. all rights reserved</div>
</footer>

</body>
</html>
```